New Record Label needs a Web design

We are Moss Lantern: a London based, new & independent music production company aimed at the 25-40 age group. The musical style is Soul/Classic Motown.
We have at the moment just one signed artist, but will expand in the future.
We dont' have any webpage yet and are looking for an innovative web design for our webpage www.moss-lantern.com
I have uploaded our company logo.

Initially the whole website will only have 3 tabs: Home page/Artists/Contact

The design should be classic and high-end, but can be a bit crazy too.

```html
<!DOCTYPE html>
<html lang="en">
<head>
<meta charset="utf-8">
<title>Moss Lantern</title>
<link href="https://fonts.googleapis.com/css2?family=Bebas+Neue&family=Questrial&family=Arimo:wght@400;700&display=swap" rel="stylesheet">
<style>
:root{
  --cream:#fbf6e3;
  --orange:#f26b35;
  --red:#e8402a;
  --black:#050505;
  --ink:#3d3d30;
  --body:#4a4538;
  --peach:#fbb08a;
  --studio-dark:#2a2826;
  --studio-mid:#6b6660;
}
*{margin:0;padding:0;box-sizing:border-box}
html,body{width:712px;height:1200px;overflow:hidden}
body{position:relative;background:var(--cream);font-family:"Arimo",Arial,sans-serif}
.abs{position:absolute}
.studio-backdrop{left:0;top:0;width:712px;height:230px;background:linear-gradient(100deg,var(--studio-mid),var(--studio-dark) 40%,#4a4744 70%,var(--studio-mid))}
.hero{left:82px;top:36px;width:549px;height:251px;background:var(--black)}
.hero-photo{left:0;top:34px;width:549px;height:217px;background:radial-gradient(ellipse at 50% 40%,#b8735a,#4a2a22 45%,#0d0b0b 75%)}
.logo-cap{left:312px;top:8px;width:96px;height:40px;background:var(--black);border-radius:48px 48px 0 0}
.logo{left:312px;top:18px;width:96px;text-align:center;font-family:"Questrial",sans-serif;font-size:11px;color:var(--red);white-space:nowrap}
.logo-dot{display:block;width:12px;height:12px;border-radius:50%;background:var(--red);margin:0 auto 2px}
.main-nav{left:94px;top:44px;display:flex;gap:21px;font-family:"Bebas Neue",sans-serif;font-size:17px;letter-spacing:.3px}
.main-nav a{color:var(--orange);text-decoration:none}
.social{left:533px;top:44px;display:flex;gap:4px}
.social span{width:15px;height:15px;border-radius:50%;background:var(--red)}
.section-title{font-family:"Bebas Neue",sans-serif;font-size:42px;line-height:1;letter-spacing:.5px}
.feature-img,.thumb{border:1px solid #222}
.feature-img{width:216px;height:157px}
.thumb{width:75px;height:54px}
.feature-name{font-family:"Questrial",sans-serif;font-weight:700;font-size:15.5px;-webkit-text-stroke:.4px currentColor;white-space:nowrap}
.item-name{font-family:"Questrial",sans-serif;font-size:11px;-webkit-text-stroke:.3px currentColor;white-space:nowrap}
.desc{font-size:6.6px;line-height:1.3;width:220px}
.more-link{font-family:"Bebas Neue",sans-serif;font-size:19px;letter-spacing:.2px}
.play{position:absolute;left:50%;top:50%;transform:translate(-50%,-50%)}
.artists .feature-name,.artists .item-name{color:var(--orange)}
.artists .desc{color:var(--body)}
.songs-band{left:0;top:688px;width:712px;height:328px;background:var(--orange)}
.fade-top{left:0;top:624px;width:712px;height:64px;background:linear-gradient(var(--cream),var(--orange))}
.fade-bottom{left:0;top:1016px;width:712px;height:60px;background:linear-gradient(var(--orange),var(--black))}
.songs .section-title,.songs .feature-name,.songs .item-name{color:#fff}
.songs .desc{color:#fde0cf}
.footer{left:0;top:1076px;width:712px;height:124px;background:var(--black)}
.foot-title{font-family:"Bebas Neue",sans-serif;font-size:30px;line-height:1}
.foot-links{display:grid;grid-template-columns:49px 40px;font-size:8px;line-height:10px;color:var(--peach)}
.foot-links a{color:var(--peach);text-decoration:none}
.signup{left:382px;top:1151px;display:flex;gap:4px}
.signup .field{width:187px;height:19px;background:var(--orange)}
.signup .btn{width:58px;height:19px;background:#fff;font-size:8px;color:#000;display:flex;align-items:center;justify-content:center}
</style>
</head>
<body>
<div class="abs studio-backdrop" role="img" aria-label="Blurred recording studio equipment"></div>

<header class="abs hero">
  <div class="abs hero-photo" role="img" aria-label="Singer wearing headphones performing at a studio microphone"></div>
</header>
<div class="abs logo-cap"></div>
<div class="abs logo"><span class="logo-dot"></span>Moss Lantern</div>
<nav class="abs main-nav"><a href="#">Home</a><a href="#">Artists</a><a href="#">Contact</a></nav>
<div class="abs social" aria-label="Social links"><span></span><span></span><span></span><span></span><span></span></div>

<section class="artists">
  <h2 class="abs section-title" style="left:84px;top:310px;color:var(--orange)">Artists</h2>
  <div class="abs feature-img" style="left:82px;top:353px;background:linear-gradient(135deg,#a9876a,#6b4a36 60%,#3a2a20)" role="img" aria-label="Artist with acoustic guitar performing outdoors"></div>
  <h3 class="abs feature-name" style="left:82px;top:519px">JONAH VALE REDDICK</h3>
  <p class="abs desc" style="left:82px;top:539px">Hit the floor and enjoy hophop DJ Orlo's spin sessions. With millions of light combinations on the dance floor, DJ Orlo will entertain with freestyle sessions.</p>

  <div class="abs thumb" style="left:325px;top:353px;background:linear-gradient(135deg,#2e3a55,#7d5a60)" role="img" aria-label="Artist portrait with red headphones"></div>
  <h3 class="abs item-name" style="left:407px;top:354px">LIRA CASTELL</h3>
  <p class="abs desc" style="left:407px;top:367px">Over 3 hours of cruising through the NYC harbor. Enjoy the open-air deck and admire magnificent views of Manhattan's stunning skyline at sunset with your sweetheart.</p>

  <div class="abs thumb" style="left:325px;top:423px;background:linear-gradient(135deg,#3f6ea8,#6f8a3a 60%,#c9a338)" role="img" aria-label="Band group photo outdoors"></div>
  <h3 class="abs item-name" style="left:407px;top:424px">RED CARPENTRY</h3>
  <p class="abs desc" style="left:407px;top:437px">Arrive on the pier and walk down the red carpet with your group. A team of professional photographers will capture your red carpet grand entrance.</p>

  <div class="abs thumb" style="left:325px;top:495px;background:linear-gradient(135deg,#3a3a3a,#8a8a84 55%,#2a2a2a)" role="img" aria-label="Band members standing together"></div>
  <h3 class="abs item-name" style="left:407px;top:496px">HAPPY YESS BAND</h3>
  <p class="abs desc" style="left:407px;top:509px">Hit the floor and enjoy hophop DJ Orlo's spin sessions. With millions of light combinations on the dance floor, DJ Orlo will entertain with freestyle sessions.</p>

  <a class="abs more-link" style="left:325px;top:578px;color:var(--ink);text-decoration:none">Click here for more gallery</a>
</section>

<div class="abs fade-top"></div>
<div class="abs songs-band"></div>
<div class="abs fade-bottom"></div>

<section class="songs">
  <h2 class="abs section-title" style="left:84px;top:703px">Songs</h2>
  <div class="abs feature-img" style="left:82px;top:746px;background:radial-gradient(circle at 30% 40%,#e8b060,#8a5020 55%,#3a2210)" role="img" aria-label="Music video still of a singer">
    <svg class="play" width="42" height="42" viewBox="0 0 42 42"><circle cx="21" cy="21" r="19" fill="none" stroke="#fff" stroke-width="2.5" opacity=".85"/><path d="M16 12 L31 21 L16 30 Z" fill="#fff" opacity=".85"/></svg>
  </div>
  <h3 class="abs feature-name" style="left:82px;top:912px">IVY MARLOWE - YOUR SONG</h3>
  <p class="abs desc" style="left:82px;top:932px">As you disembark you will receive your custom gift bag to take home with you which will include souvenirs.</p>

  <div class="abs thumb" style="left:325px;top:746px;background:linear-gradient(135deg,#e89048,#c24a20)" role="img" aria-label="Music video still">
    <svg class="play" width="30" height="30" viewBox="0 0 30 30"><circle cx="15" cy="15" r="13" fill="none" stroke="#fff" stroke-width="2"/><path d="M11 8 L22 15 L11 22 Z" fill="#fff"/></svg>
  </div>
  <h3 class="abs item-name" style="left:407px;top:747px">MARNIE HALE - OUR SONG</h3>
  <p class="abs desc" style="left:407px;top:760px">Over 3 hours of cruising through the NYC harbor. Enjoy the open-air deck and admire magnificent views of Manhattan's stunning skyline at sunset with your sweetheart.</p>

  <div class="abs thumb" style="left:325px;top:816px;background:linear-gradient(135deg,#6a4a3a,#3c5a90 60%,#c8c0b0)" role="img" aria-label="Music video still of a boy band">
    <svg class="play" width="30" height="30" viewBox="0 0 30 30"><circle cx="15" cy="15" r="13" fill="none" stroke="#fff" stroke-width="2" opacity=".8"/><path d="M11 8 L22 15 L11 22 Z" fill="#fff" opacity=".8"/></svg>
  </div>
  <h3 class="abs item-name" style="left:407px;top:817px">BOY BAND NEXT WALL</h3>
  <p class="abs desc" style="left:407px;top:830px">Savor the taste of an exquisite delicacies created by our executive chef exclusively for this event.</p>

  <div class="abs thumb" style="left:325px;top:888px;background:linear-gradient(135deg,#2f5a2a,#c9b8a0 55%,#2a3a20)" role="img" aria-label="Music video still of a dancer">
    <svg class="play" width="30" height="30" viewBox="0 0 30 30"><circle cx="15" cy="15" r="13" fill="none" stroke="#fff" stroke-width="2" opacity=".8"/><path d="M11 8 L22 15 L11 22 Z" fill="#fff" opacity=".8"/></svg>
  </div>
  <h3 class="abs item-name" style="left:407px;top:889px">PERSONALIZED GIFT BAG</h3>
  <p class="abs desc" style="left:407px;top:902px">As you disembark you will receive your custom gift bag to take home with you which will include souvenirs.</p>

  <a class="abs more-link" style="left:325px;top:965px;color:var(--peach);text-decoration:none">Click here for more songs</a>
</section>

<footer class="abs footer">
  <div class="abs" style="left:0;top:28px;width:250px;">
    <div style="position:absolute;left:78px;top:0;width:96px;text-align:center;font-family:'Questrial',sans-serif;font-size:11px;color:var(--red);white-space:nowrap"><span class="logo-dot"></span>Moss Lantern</div>
  </div>
  <p class="abs" style="left:99px;top:73px;font-size:6.5px;color:var(--orange)">Copyright © 2014</p>
  <h2 class="abs foot-title" style="left:220px;top:27px;color:var(--orange)">Navigation</h2>
  <nav class="abs foot-links" style="left:221px;top:58px"><a href="#">Home</a><a href="#">Songs</a><a href="#">Artists</a><a href="#">Contact</a></nav>
  <h2 class="abs foot-title" style="left:381px;top:27px;color:var(--red)">Connect with Moss Lantern</h2>
  <p class="abs" style="left:383px;top:58px;font-size:9px;color:var(--orange)"><b style="color:var(--red)">subscribe</b> to our newsletter</p>
</footer>
<div class="abs signup"><div class="field"></div><div class="btn">Subscribe</div></div>
</body>
</html>
```